Tea bag packaging design for KELVIRA

Hello. I am creating a green tea and soybean tea, and I am looking for packaging designs. I will attach some designs I like and our current KELVIRA logo. Feel free to follow the designs or create something of your own.

Package size is 200 (W) x 290(L) mm

The package is a white aluminum package so it can accommodate a wide range of colors. We don't want to pay a ton in printing so 5 colors or less is nice. But we will make exceptions for something more colorful if it's well done.

Target Market(s)

Women and Men in 30s-40s

Industry/Entity Type

food and beverage

Font styles to use
Sans Serif
Other font styles liked:
• red hat is the font of the logo

Requirements
Must have
• clean, simple, but bold design
Nice to have
• images of soybeans and green tea leaves on the package

```html
<!DOCTYPE html>
<html lang="en">
<head>
<meta charset="utf-8">
<title>KELVIRA Green &amp; Soybean Tea – Pouch Front</title>
<link rel="stylesheet" href="https://fonts.googleapis.com/css2?family=Red+Hat+Display:wght@300;400;500;700;800;900&display=swap">
<style>
  :root {
    --backdrop: #e9eae8;
    --pouch-white: #ffffff;
    --pouch-shade: #eceeed;
    --ink: #111111;
    --ink-soft: #3a3a3a;
    --lime: #c3d332;
    --lime-light: #e3ec8c;
    --leaf: #4f8f2a;
  }
  * { box-sizing: border-box; margin: 0; padding: 0; }
  html, body {
    width: 1200px;
    height: 952px;
    overflow: hidden;
    background: var(--backdrop);
    font-family: "Red Hat Display", Arial, sans-serif;
  }
  .pouch {
    position: absolute;
    left: 292px;
    top: 36px;
    width: 616px;
    height: 880px;
    background: linear-gradient(180deg, var(--pouch-shade) 0%, var(--pouch-white) 12%, var(--pouch-white) 100%);
    overflow: hidden;
  }
  .zip-seal {
    position: absolute;
    left: 0; right: 0;
    top: 78px;
    height: 6px;
    border-top: 1px solid #dcdedd;
    border-bottom: 1px solid #dcdedd;
  }
  .brand {
    position: absolute;
    left: 62px;
    top: 140px;
    display: flex;
    align-items: center;
    gap: 10px;
    font-weight: 800;
    font-size: 27px;
    letter-spacing: 0.5px;
    color: var(--ink);
  }
  .brand-dot {
    width: 14px;
    height: 14px;
    border-radius: 50%;
    background: var(--ink);
  }
  .title {
    position: absolute;
    left: 50px;
    top: 234px;
    font-family: "Red Hat Display", Arial, sans-serif;
    font-weight: 800;
    font-size: 60px;
    line-height: 63px;
    letter-spacing: -1px;
    white-space: nowrap;
  }
  .title-green { color: var(--lime); display: block; font-weight: 800; }
  .title-main { color: var(--ink); display: block; font-weight: 800; }
  .tagline {
    position: absolute;
    left: 52px;
    top: 373px;
    font-weight: 300;
    font-size: 20px;
    line-height: 25px;
    color: var(--ink-soft);
  }
  .caffeine {
    position: absolute;
    left: 53px;
    top: 477px;
    display: flex;
    align-items: center;
    gap: 12px;
    font-weight: 500;
    font-size: 11px;
    color: var(--ink);
  }
  .caffeine-dots { display: flex; gap: 4px; }
  .caffeine-dots span {
    width: 12px;
    height: 7px;
    border-radius: 0 0 7px 7px;
    background: var(--lime);
  }
  .flavour-panel {
    position: absolute;
    left: 271px;
    top: 380px;
    right: 0;
    bottom: 0;
    overflow: hidden;
    background: linear-gradient(160deg, var(--lime-light) 0%, var(--lime) 60%, #b9cb2a 100%);
  }
  .product-photo {
    position: absolute;
    inset: 0;
    background:
      radial-gradient(ellipse 45% 30% at 50% 55%, rgba(150, 185, 60, 0.85), rgba(150, 185, 60, 0) 100%),
      radial-gradient(ellipse 35% 30% at 85% 20%, rgba(79, 143, 42, 0.75), rgba(79, 143, 42, 0) 100%),
      radial-gradient(ellipse 25% 10% at 15% 82%, rgba(110, 90, 55, 0.5), rgba(110, 90, 55, 0) 100%);
  }
  .net-weight {
    position: absolute;
    left: 50px;
    top: 830px;
    font-weight: 500;
    font-size: 17px;
    color: var(--ink);
  }
</style>
</head>
<body>
  <main class="pouch">
    <div class="zip-seal"></div>

    <div class="brand"><span class="brand-dot"></span>KELVIRA</div>

    <h1 class="title">
      <span class="title-green">GREEN &amp;</span>
      <span class="title-main">SOYBEAN TEA</span>
    </h1>

    <p class="tagline">Handcrafted for<br>Natural Refreshment<br>and Vitality</p>

    <div class="caffeine">
      <span>Caffeine Level</span>
      <div class="caffeine-dots"><span></span><span></span><span></span><span></span><span></span></div>
    </div>

    <div class="flavour-panel">
      <div class="product-photo" role="img" aria-label="Glass cup of green tea with fresh tea leaves, a small bowl of soybeans and scattered green beans"></div>
    </div>

    <p class="net-weight">NET WEIGHT: 200G</p>
  </main>
</body>
</html>
```